Medical Prescription for Diagnostic Sleep Testing

Quiet Harbor Rest Labs main marketing tool is our Prescription that we leave with medical providers. Prescription is printed on 8.5 x 11 sheets of paper to create a prescription pad for our medical providers. Prescription should fit to one page. Quiet Harbor Rest Labs works with 250 different medical providers so it is important we are able to update and change the medical provider information at bottom. The medical provider would fill-out top with patient information, check-off center testing and patient co-morbidity and Fax to Quiet Harbor Rest Labs. Because it is Faxed to us it is important to have clear print and large font Attached or uploaded file is one example we currently use. Please review all 5 must haves.

Target Market(s)

Prescription for medical providers to fill-out and fax to Quiet Harbor Rest Labs to conduct the sleep study.

Industry/Entity Type

Medical

Colors

Designer to choose only greyscale colors for use in the design.

Requirements
Must have
• 1) Prescription Size: 8.5 x 11
• 2) Must fit to One page Only
• 3) Ability to change medical provider information at bottom of prescription. We work with 250 different medical providers
• 4) Ability to change or update any part of prescription
• 5) Document Must be created in Microsoft Word 2016. This is the program we use for our prescriptions.
Nice to have
• Can be done in Gray-Scale or Black and White since its being faxed from the medical provider to us.

```html
<!DOCTYPE html>
<html lang="en">
<head>
<meta charset="utf-8">
<title>Sleep Study Physician Order</title>
<link href="https://fonts.googleapis.com/css2?family=Montserrat:wght@600;700;800&family=Roboto:ital,wght@0,400;0,500;0,700;1,400;1,500;1,700&display=swap" rel="stylesheet">
<style>
  :root{
    --bg:#e4e4e8;
    --paper:#ededef;
    --ink:#111;
    --purple:#5a2890;
    --band:#c6c6c9;
    --cream:#e8dfc3;
  }
  html,body{margin:0;padding:0;width:1180px;height:1200px;overflow:hidden;background:var(--bg);}
  body{font-family:"Roboto",Arial,sans-serif;color:var(--ink);}
  .page{position:absolute;left:140px;top:14px;width:900px;height:1172px;background:var(--paper);box-shadow:0 2px 10px rgba(0,0,0,.12);}
  .abs{position:absolute;}
  .brand{left:44px;top:58px;width:170px;height:96px;display:flex;align-items:center;gap:8px;}
  .brand-mark{width:14px;height:14px;background:var(--purple);flex:none;}
  .brand-name{font-family:"Montserrat",sans-serif;font-weight:700;font-size:19px;line-height:1.15;color:var(--purple);}
  .header{left:216px;top:40px;width:640px;text-align:center;}
  .title{font-family:"Montserrat",sans-serif;font-weight:800;font-size:33px;color:var(--purple);margin:0;letter-spacing:.2px;}
  .phone{font-weight:700;font-style:italic;font-size:23px;margin-top:2px;}
  .addr{font-weight:700;font-style:italic;font-size:15px;margin-top:4px;}
  .addr u{font-weight:700;}
  .fields{left:48px;width:810px;}
  .row{display:flex;align-items:flex-end;font-weight:700;font-size:14px;height:20px;position:absolute;left:0;width:100%;}
  .line{flex:1;border-bottom:1.5px solid #222;margin:0 4px 3px;}
  .band{left:38px;width:825px;background:var(--band);font-family:"Montserrat",sans-serif;font-weight:700;text-align:center;}
  .box{display:inline-block;width:14px;height:14px;border:2px solid var(--purple);border-radius:2px;box-sizing:border-box;flex:none;}
  .opt{left:60px;width:800px;display:flex;gap:12px;}
  .opt .box{margin-top:3px;}
  .opt-title{font-weight:700;font-size:17px;}
  .note{font-style:italic;font-size:12px;font-weight:400;}
  .sub{font-weight:700;font-size:14px;padding-left:32px;line-height:1.15;}
  .sub2{font-size:12px;font-style:italic;padding-left:32px;line-height:1.3;}
  .conds{left:60px;top:696px;width:800px;display:grid;grid-template-columns:307px 262px 230px;}
  .conds ul{list-style:none;margin:0;padding:0;}
  .conds li{display:flex;gap:9px;font-style:italic;font-size:14px;line-height:19.5px;}
  .conds .box{width:11px;height:11px;border-width:1.5px;margin-top:4px;}
  .prov-band{top:876px;height:36px;text-align:left;display:flex;align-items:center;justify-content:space-between;padding:0 30px;box-sizing:border-box;}
  .prov-band .name{font-size:25px;letter-spacing:.5px;}
  .prov-band .contact{font-family:"Roboto",sans-serif;font-style:italic;font-size:12px;line-height:1.35;}
  .doctors{left:60px;top:930px;width:800px;display:grid;grid-template-columns:280px 265px 255px;row-gap:10px;}
  .doc{display:flex;gap:14px;}
  .doc .box{width:16px;height:16px;margin-top:2px;}
  .doc b{font-size:16px;display:block;}
  .doc span{font-size:14px;font-weight:700;color:#333;}
  .sig{left:28px;top:1042px;width:830px;display:flex;align-items:flex-end;font-weight:700;font-size:15px;}
  .sig .line{margin-bottom:2px;}
  .footer{left:0;top:1067px;width:900px;height:60px;background:var(--cream);text-align:center;}
  .footer .f1{font-weight:700;font-size:15px;margin-top:7px;}
  .footer .f2{font-family:"Montserrat",sans-serif;font-weight:700;font-size:20px;margin-top:2px;}
  .thanks{left:0;top:1144px;width:900px;text-align:center;font-size:13px;}
</style>
</head>
<body>
<div class="page">
  <div class="abs brand">
    <span class="brand-mark"></span>
    <span class="brand-name">Quiet Harbor Rest Labs</span>
  </div>

  <header class="abs header">
    <h1 class="title">SLEEP STUDY PHYSICIAN ORDER</h1>
    <div class="phone">Phone: (555) 210-4480 &nbsp;•&nbsp; Fax: (555) 210-4481</div>
    <div class="addr">820 W. Lantern Avenue, Suite 2 - C; Brightwater, NV 89000</div>
    <div class="addr">Email: <u>intake@quietharborrest.example</u> • Website: quietharborrest.example</div>
  </header>

  <section class="abs fields" style="top:0;">
    <div class="row" style="top:178px;">Patient Name:<span class="line" style="flex:2.6"></span>DOB:<span class="line" style="flex:.45;margin-right:0"></span>/<span class="line" style="flex:.45;margin:0 0 3px"></span>/<span class="line" style="flex:.55;margin-right:0"></span></div>
    <div class="row" style="top:209px;">Telephone:<span class="line"></span>Alternate Telephone:<span class="line"></span></div>
    <div class="row" style="top:240px;">Primary Insurance:<span class="line"></span>Secondary Insurance:<span class="line"></span></div>
    <div class="row" style="top:271px;">Height:<span class="line"></span>Weight:<span class="line" style="flex:1.2"></span>Patient Gender (circle one): &nbsp; M &nbsp;/&nbsp; F</div>
  </section>

  <div class="abs band" style="top:314px;height:30px;line-height:30px;font-size:20px;">DIAGNOSTIC SLEEP STUDY</div>

  <div class="abs opt" style="top:362px;display:block;">
    <div style="display:flex;gap:12px;"><span class="box"></span><span class="opt-title">COMPLETE SLEEP STUDY: <span class="note" style="font-size:14px;text-decoration:underline">(Based on Insurance or Patient's Choice)</span></span></div>
    <div class="sub">In-Lab Sleep Study (PSG) or Home Sleep Study <span class="note">(PSG 95810 / HST 95806)</span></div>
    <div class="sub">with follow-up PAP Titration Study <span class="note">(PAP 95811 if positive for sleep apnea)</span></div>
  </div>
  <div class="abs opt" style="top:428px;display:block;">
    <div style="display:flex;gap:12px;"><span class="box"></span><span class="opt-title">PEDIATRIC SLEEP STUDY: PSG w/End Tidal CO2 Monitoring</span></div>
    <div class="sub2">(PSG 95782 under 6 years of age &amp; PSG 95810 older than 6 years of age)</div>
  </div>
  <div class="abs opt" style="top:483px;"><span class="box"></span><span class="opt-title">In-Lab Diagnostic Sleep Study/Polysomnogram <span class="note">(PSG 95810)</span></span></div>
  <div class="abs opt" style="top:521px;display:block;">
    <div style="display:flex;gap:12px;"><span class="box"></span><span class="opt-title">SPLIT-NIGHT STUDY <span class="note">(PSG with PAP 95810 &amp; 95811)</span></span></div>
    <div class="sub2"><b><u>To Comply with Accreditation &amp; Insurance Guidelines</u></b>: AHI must be 20 or greater with minimum 2 hour recorded sleep time<br>and 3 hours minimum to complete PAP treatment.</div>
  </div>
  <div class="abs opt" style="top:593px;"><span class="box"></span><span class="opt-title">CPAP / BiPAP / BiPAP ST Titration Study <span class="note">(Patients with documented sleep apnea 95811)</span></span></div>
  <div class="abs opt" style="top:631px;"><span class="box"></span><span class="opt-title">Home Sleep Study <span class="note">(HST 95806/G0399 Adults Only, Conducted Unattended at Patient Home)</span></span></div>

  <div class="abs band" style="top:657px;height:28px;line-height:28px;font-size:18.5px;">PATIENT MEDICAL NECESSITY – DIAGNOSIS / MEDICAL HISTORY / SYMPTOMS</div>

  <section class="abs conds">
    <ul>
      <li><span class="box"></span>Atrial Fibrillation</li>
      <li><span class="box"></span>Bipolar Disorder</li>
      <li><span class="box"></span>Congestive Heart Failure</li>
      <li><span class="box"></span>COPD</li>
      <li><span class="box"></span>Depression</li>
      <li><span class="box"></span>Excessive Daytime Sleepiness</li>
      <li><span class="box"></span>Gasping Sensations with Frequent<br>Awakenings</li>
      <li><span class="box"></span>Frequent Urination</li>
    </ul>
    <ul>
      <li><span class="box"></span>Heart Disease</li>
      <li><span class="box"></span>History Heart Attack</li>
      <li><span class="box"></span>Hypertension</li>
      <li><span class="box"></span>Insomnia</li>
      <li><span class="box"></span>Mental or Mood Disorder</li>
      <li><span class="box"></span>Loud Snoring</li>
      <li><span class="box"></span>Morbid Obesity / Obesity</li>
      <li><span class="box"></span>Morning Headaches</li>
      <li><span class="box"></span>Narcolepsy</li>
    </ul>
    <ul>
      <li><span class="box"></span>Opioid Use</li>
      <li><span class="box"></span>PTSD</li>
      <li><span class="box"></span>Pulmonary Disease</li>
      <li><span class="box"></span>Restless Leg Syndrome</li>
      <li><span class="box"></span>Seizures</li>
      <li><span class="box"></span>Shift Work Sleep disorder</li>
      <li><span class="box"></span>Stroke / TIA</li>
      <li><span class="box"></span>Witnessed Apnea</li>
      <li><span class="box"></span>Other: ______________</li>
    </ul>
  </section>

  <div class="abs band prov-band">
    <span class="name">MESA VALLEY AIRWAY CLINIC</span>
    <span class="contact"><b>415 N. Canyon Drive; Brightwater, NV 89001-2200<br>Telephone: 555-318-2290 Fax: 555-318-2291</b></span>
  </div>

  <section class="abs doctors">
    <div class="doc"><span class="box"></span><div><b>Dr. Miles Andrew Corbett</b><span>NPI: 1000000011</span></div></div>
    <div class="doc"><span class="box"></span><div><b>Dr. Helena R. Vance</b><span>NPI: 1000000029</span></div></div>
    <div class="doc"><span class="box"></span><div><b>Dr Owen P. Lindqvist</b><span>NPI: 1000000037</span></div></div>
    <div class="doc"><span class="box"></span><div><b>Dr. Nora Blake</b><span>NPI: 1000000045</span></div></div>
    <div class="doc"><span class="box"></span><div><b>Irene Castell, FNP-C</b><span>NPI: 1000000052</span></div></div>
    <div class="doc"><span class="box"></span><div><b>Paul Dorsey, PA-C</b><span>NPI: 1000000060</span></div></div>
  </section>

  <div class="abs sig">Physician's Signature:<span class="line" style="flex:4"></span>Date:<span class="line" style="flex:.3;margin-right:0"></span>/<span class="line" style="flex:.3;margin:0 0 2px"></span>/<span class="line" style="flex:.35;margin-right:20px"></span></div>

  <footer class="abs footer">
    <div class="f1">Please Fax: 555-210-4481 or Email: <u>intake@quietharborrest.example</u></div>
    <div class="f2">Fax Along With: Clinical Notes &nbsp;•&nbsp; Insurance &nbsp;•&nbsp; Demographic Information</div>
  </footer>
  <div class="abs thanks">THANK YOU FOR YOUR SUPPORT ELIAS &amp; MARCO</div>
</div>
</body>
</html>
```